Business Card Design Project

looking for a stylish and simple double sided business card.
I am an artist - specialising in fashion illustration, portraits and murals.
the front should be simply my name and tag:

D U R E S K
Living in colour

My preference is for a Black background with DURESK in red or embossed.
Living in colour in White or multi-coloured.

the back will have detail:

Personalised Art
Portraits, Murals, Fashion Illustration

0437 582 190
duresk@duresk.com.au
www.duresk.com.au

Target Market(s)

Adults that are based in western speaking countries who have an appreciation for art and design. Portraits and wall art
Business owners who may need personalised all art for their business space. Murals and personalised canvass.
People in the fashion industry, who may require fashion illustrations.

Industry/Entity Type

Fashion

Requirements
Must have
• BOLD but simple at the same time, timeless modern element to it.
Nice to have
• simple lettering
Should not have
• Not too busy or wordy,

```html
<!DOCTYPE html>
<html lang="en">
<head>
<meta charset="utf-8">
<title>Duresk — Business Card</title>
<link rel="stylesheet" href="https://fonts.googleapis.com/css2?family=Bebas+Neue&family=Yellowtail&family=Poiret+One&display=swap">
<style>
  :root {
    --card-base: #2b2a2c;
    --card-dark: #1c1c1e;
    --tint-rose: #8a4a5a;
    --tint-plum: #6b4f68;
    --tint-olive: #6a6448;
    --accent-red: #d22b52;
    --ink-white: #ffffff;
    --rule-grey: #d9d9d9;
    --gap-white: #f4f4f4;
  }
  html, body {
    margin: 0;
    padding: 0;
    width: 923px;
    height: 1200px;
    overflow: hidden;
    background: var(--gap-white);
  }
  .business-card-sheet {
    display: block;
    width: 923px;
    height: 1200px;
  }
  .brand-name {
    font-family: "Bebas Neue", sans-serif;
    font-size: 176px;
    letter-spacing: 0.12em;
    fill: var(--ink-white);
  }
  .tagline, .service-title {
    font-family: "Yellowtail", cursive;
    fill: var(--accent-red);
  }
  .tagline { font-size: 46px; }
  .service-title { font-size: 50px; letter-spacing: 0.02em; }
  .contact-line {
    font-family: "Bebas Neue", sans-serif;
    fill: var(--ink-white);
  }
  .contact-phone { font-size: 84px; letter-spacing: 0.03em; }
  .contact-email { font-size: 56px; }
  .contact-web { font-size: 70px; }
  .services-list {
    font-family: "Poiret One", sans-serif;
    font-size: 34px;
    fill: var(--ink-white);
  }
  .divider { stroke: var(--rule-grey); stroke-width: 1.6; }
</style>
</head>
<body>
<svg class="business-card-sheet" viewBox="0 0 923 1200" xmlns="http://www.w3.org/2000/svg">
  <defs>
    <linearGradient id="card-shade" x1="0" y1="0" x2="1" y2="1">
      <stop offset="0" stop-color="var(--card-base)"/>
      <stop offset="0.5" stop-color="var(--card-dark)"/>
      <stop offset="1" stop-color="var(--card-base)"/>
    </linearGradient>
    <radialGradient id="glow-rose" cx="0.05" cy="0.05" r="0.6">
      <stop offset="0" stop-color="var(--tint-rose)" stop-opacity="0.75"/>
      <stop offset="1" stop-color="var(--tint-rose)" stop-opacity="0"/>
    </radialGradient>
    <radialGradient id="glow-olive" cx="0.02" cy="0.85" r="0.45">
      <stop offset="0" stop-color="var(--tint-olive)" stop-opacity="0.6"/>
      <stop offset="1" stop-color="var(--tint-olive)" stop-opacity="0"/>
    </radialGradient>
    <radialGradient id="glow-plum" cx="0.95" cy="0.9" r="0.5">
      <stop offset="0" stop-color="var(--tint-plum)" stop-opacity="0.6"/>
      <stop offset="1" stop-color="var(--tint-plum)" stop-opacity="0"/>
    </radialGradient>
  </defs>

  <!-- Front of card -->
  <g class="card-front">
    <rect x="0" y="0" width="923" height="596" fill="url(#card-shade)"/>
    <rect x="0" y="0" width="923" height="596" fill="url(#glow-rose)"/>
    <rect x="0" y="0" width="923" height="596" fill="url(#glow-olive)"/>
    <rect x="0" y="0" width="923" height="596" fill="url(#glow-plum)"/>
    <polygon points="340,0 923,0 923,260 600,420" fill="#ffffff" opacity="0.025"/>
    <polygon points="0,300 420,596 0,596" fill="#000000" opacity="0.08"/>
    <text class="brand-name" x="472" y="309" text-anchor="middle">DURESK</text>
    <line class="divider" x1="213" y1="343" x2="704" y2="343"/>
    <text class="tagline" x="461" y="401" text-anchor="middle">living in colour</text>
  </g>

  <!-- Back of card -->
  <g class="card-back">
    <rect x="0" y="602" width="923" height="598" fill="url(#card-shade)"/>
    <rect x="0" y="602" width="923" height="598" fill="url(#glow-plum)"/>
    <polygon points="500,602 923,602 923,760" fill="#ffffff" opacity="0.03"/>
    <polygon points="0,700 360,1200 0,1200" fill="#000000" opacity="0.08"/>
    <text class="service-title" x="461" y="747" text-anchor="middle">Personalised  Art</text>
    <line class="divider" x1="271" y1="778" x2="651" y2="778"/>
    <text class="contact-line contact-phone" x="463" y="870" text-anchor="middle">0437 582 190</text>
    <text class="contact-line contact-email" x="463" y="941" text-anchor="middle">duresk@duresk.com.au</text>
    <text class="contact-line contact-web" x="463" y="1015" text-anchor="middle">www.duresk.com.au</text>
    <line class="divider" x1="273" y1="1042" x2="655" y2="1042"/>
    <text class="services-list" x="65" y="1171" textLength="791" lengthAdjust="spacing">PORTRAITS • MURALS •  FASHION ILLUSTRATION</text>
  </g>
</svg>
</body>
</html>
```